Buch-Cover für Sonnenherz gesucht
Der Designer hat sich sehr schnell in meine Vorgaben eingearbeitet und gleichzeitig wertvolle Vorschläge zur Optimierung abgegeben. Das Ergebnis ist dadurch sogar besser geworden, als ich mir im Vorfeld ausgemalt hatte. 100% Weiterempfehlung.
Zielgruppe
Wir sind eine Firma die hochwertige Fitnessprodukte produziert und vertreibt. Unsere Zielgruppe sind gesundheitsbewusste Frauen ab Mitte 20 bis open end, die hohe Ansprüche an sich selbst stellen und sich für das Thema Selbstoptimierung interessieren.
Aufgabenstellung
Es soll ein Hardcover gestaltet werden.
Buchtitel: Sonnenherz, Untertitel: Das Erwachen der Seele
Detaillierte Beschreibung der Projektanforderungen siehe Anhang Projektbeschreibung. Darüber hinaus bin ich auch für alternative Gestaltungs-Ideen offen.
Das Design soll der Käuferin folgendes vermitteln:
- Wertigkeit
- Positivität
und sie ein bisschen träumen lassen und natürlich neugierig auf den Inhalt machen.

```html
<!DOCTYPE html>
<html lang="de">
<head>
<meta charset="utf-8">
<title>Sonnenherz – Buchumschlag</title>
<link href="https://fonts.googleapis.com/css2?family=Great+Vibes&family=Lobster+Two:ital,wght@1,700&family=Oswald:wght@400&family=Fira+Sans+Condensed:wght@400&family=Montserrat:wght@800&display=swap" rel="stylesheet">
<style>
  :root {
    --page-bg: #ffffff;
    --navy: #1c3a6b;
    --teal: #1e8585;
    --teal-deep: #17716f;
    --peach: #f3c9a0;
    --amber: #e8a066;
    --cream: #fbeedd;
    --white: #ffffff;
    --rust: #c8622c;
    --spine-yellow: #f2c75a;
    --spine-navy: #183a66;
  }
  * { margin: 0; padding: 0; box-sizing: border-box; }
  html, body { width: 1200px; height: 808px; overflow: hidden; background: var(--page-bg); }
  .cover {
    position: absolute; left: 68px; top: 46px; width: 1066px; height: 716px;
    display: flex; box-shadow: 8px 8px 10px rgba(0,0,0,0.45);
  }
  .back { position: relative; width: 520px; height: 100%; overflow: hidden; }
  .spine { position: relative; width: 40px; height: 100%; background: var(--teal); border-right: 1px solid rgba(255,255,255,0.6); }
  .front { position: relative; width: 506px; height: 100%; overflow: hidden; }

  .back-backdrop {
    position: absolute; inset: 0;
    background:
      radial-gradient(ellipse 60% 35% at 60% 30%, rgba(246,200,150,0.85), rgba(246,200,150,0) 70%),
      linear-gradient(180deg, var(--navy) 0%, #4a6a8a 16%, #c9a48a 34%, #3f9a92 50%, var(--teal) 70%, var(--teal-deep) 100%);
  }
  .back-title {
    position: absolute; left: 0; width: 100%; top: 95px; text-align: center;
    font-family: "Great Vibes", cursive; font-size: 80px; line-height: 96px; color: var(--cream);
  }
  .back-heading {
    position: absolute; left: 0; width: 100%; top: 296px; text-align: center;
    font-family: "Oswald", sans-serif; font-size: 27px; line-height: 36px; letter-spacing: 3px; color: var(--cream);
  }
  .blurb {
    position: absolute; left: 42px; width: 438px; top: 350px;
    font-family: "Fira Sans Condensed", sans-serif; font-size: 12.3px; line-height: 19.4px;
    letter-spacing: -0.1px; color: var(--white); text-align: justify;
  }
  .blurb p + p { margin-top: 19.4px; }

  .spine-text {
    position: absolute; left: 0; width: 40px; writing-mode: vertical-rl;
    display: flex; align-items: center; justify-content: center;
  }
  .spine-author { top: 14px; height: 128px; font-family: "Lobster Two", cursive; font-style: italic; font-size: 16px; color: var(--spine-navy); }
  .spine-title { top: 152px; height: 200px; font-family: "Montserrat", sans-serif; font-weight: 800; font-size: 24px; letter-spacing: 2px; color: var(--spine-navy); }
  .spine-subtitle { top: 362px; height: 336px; font-family: "Lobster Two", cursive; font-style: italic; font-weight: 700; font-size: 23px; color: var(--spine-yellow); }

  .front-backdrop {
    position: absolute; inset: 0;
    background:
      radial-gradient(ellipse 55% 25% at 45% 52%, rgba(255,214,160,0.9), rgba(255,214,160,0) 70%),
      linear-gradient(180deg, var(--navy) 0%, #3b5b80 14%, #b49a92 30%, var(--peach) 44%, var(--amber) 52%, #6a5a55 64%, #3c3c44 80%, #26262e 100%);
  }
  .front-author {
    position: absolute; left: 0; width: 100%; top: 26px; text-align: center;
    font-family: "Lobster Two", cursive; font-style: italic; font-weight: 700; font-size: 36px; line-height: 46px; color: var(--white);
  }
  .front-title {
    position: absolute; left: 0; width: 100%; top: 108px; text-align: center;
    font-family: "Great Vibes", cursive; font-size: 112px; line-height: 134px; color: var(--white);
    text-shadow: 0 0 14px rgba(255,255,255,0.5);
  }
  .front-subtitle {
    position: absolute; left: 0; width: 100%; top: 250px; text-align: center;
    font-family: "Lobster Two", cursive; font-style: italic; font-weight: 700; font-size: 28px; line-height: 32px; color: var(--rust);
  }
  .publisher {
    position: absolute; left: 0; width: 100%; top: 672px; text-align: center;
    font-family: "Fira Sans Condensed", sans-serif; font-size: 16px; color: var(--white);
  }
</style>
</head>
<body>
  <div class="cover">
    <section class="back">
      <div class="back-backdrop" role="img" aria-label="Sonnenlicht mit goldenen Bokeh-Lichtern über blau-türkisem Himmel"></div>
      <div class="back-title">Sonnenherz</div>
      <div class="back-heading">Was zählt wirklich?</div>
      <div class="blurb">
        <p>Ich habe mich oft gefragt: Wie soll ich bloß die Liebe und Bestätigung, die mir damals in meiner Kindheit verwehrt blieben, "nachholen"? Lösungsansätze für mein Problem hatte in der Vergangenheit durchaus: Ich versuchte das Loch in peace with Hilfe zur Selbsthilfe, Erfolg im Job und Konsum zu stopfen. Und meine Partner mussten auch für so einiges herhalten.</p>
        <p>Von Gott wollte ich lange nichts wissen. Schließlich hatte er es zugelassen, dass mir sehr viel Unheil in meinem Leben widerfahren ist. Und deshalb war ich echt wütend auf ihn.</p>
        <p>Heutzutage bin ich mir sicher, dass ich mit dieser Denkweise meine Lebenszeit verschwendet habe. Letzten Sommer begriff ich endlich: im Leben gilt die gleiche Gesetzmäßigkeit wie beim Autofahren. Der Rückspiegel ist so klein und die Frontscheibe so groß, weil das, was vor uns liegt, viel wichtiger ist als das, was hinter uns liegt. Aufgrund dieser Erkenntnis entschied ich mich, einen völlig neuen Weg einzuschlagen und wagte mich auf eine spannende Reise, die mein Leben für immer veränderte ...</p>
      </div>
    </section>

    <section class="spine">
      <div class="spine-text spine-author">Mara Feltkamp</div>
      <div class="spine-text spine-title">SONNENHERZ</div>
      <div class="spine-text spine-subtitle">Das Erwachen der Seele</div>
    </section>

    <section class="front">
      <div class="front-backdrop" role="img" aria-label="Foto: Frau von hinten am Steuer eines Cabrios auf einem Feldweg im Abendlicht, mit Bokeh-Lichtern"></div>
      <div class="front-author">Mara Feltkamp</div>
      <div class="front-title">Sonnenherz</div>
      <div class="front-subtitle">Das Erwachen<br>der Seele</div>
      <div class="publisher">Lichtweg</div>
    </section>
  </div>
</body>
</html>
```